New custom software business needs a Wordpress site

We need a Wordpress site for a new company based out of Chicago called 'Vellora Consulting'. Using a mix of on and off-shore resources we build custom software solutions, mainly focusing on small to medium sized companies. We help our customers "aspire" to do great things.
We have a basic site up here: https://brindlewave.example/. We worked on the content for it but not the branding. For now, this houses all the pages (except for a Contact Us page we'll be adding soon) for the foreseeable future.
We also have a new logo (attached) that we'd like to base the styling/colors on.
Target Market(s)
Small to medium sized companies that require tech resources
Industry/Entity Type
Software
Nice to have
- Teamwork, tech, professional but not elitist

```html
<!DOCTYPE html>
<html lang="en">
<head>
<meta charset="utf-8">
<title>Vellora Consulting — Business Planning &amp; Software Consultant</title>
<link href="https://fonts.googleapis.com/css2?family=Lato:wght@400;700;900&display=swap" rel="stylesheet">
<style>
  :root {
    --blue-deep: #0a4ea6;
    --blue-band: #0055a8;
    --blue-hero-a: #0b57b0;
    --blue-hero-b: #1a4f98;
    --card-bg: rgba(12, 48, 104, 0.62);
    --white: #ffffff;
    --muted-white: rgba(255, 255, 255, 0.78);
    --heading-dark: #3d4a6b;
    --body-grey: #9a9fae;
    --btn-grad-a: #2f7bd0;
    --btn-grad-b: #0b4fa8;
    --btn-light: #3d86f0;
  }
  * { box-sizing: border-box; margin: 0; padding: 0; }
  html, body { width: 1025px; height: 1200px; overflow: hidden; background: var(--white); }
  body { font-family: "Lato", sans-serif; position: relative; }

  .hero { position: absolute; left: 0; top: 0; width: 1025px; height: 560px; overflow: hidden; }
  .hero-photo {
    position: absolute; inset: 0;
    background:
      radial-gradient(ellipse at 70% 40%, rgba(60,130,210,0.55), transparent 60%),
      radial-gradient(ellipse at 25% 75%, rgba(90,150,220,0.35), transparent 55%),
      linear-gradient(135deg, var(--blue-hero-a), var(--blue-hero-b));
  }
  .hero-eyebrow { position: absolute; left: 132px; top: 60px; font-size: 8.5px; color: var(--muted-white); }
  .hero-title { position: absolute; left: 131px; top: 78px; font-size: 41px; line-height: 52px; font-weight: 700; color: var(--white); letter-spacing: -0.3px; }
  .hero-lead { position: absolute; left: 132px; top: 190px; width: 420px; font-size: 9.6px; line-height: 19px; color: var(--white); }
  .hero-actions { position: absolute; left: 132px; top: 252px; display: flex; gap: 15px; }
  .btn-outline, .btn-solid { height: 28px; font-size: 10px; font-weight: 700; color: var(--white); display: flex; align-items: center; justify-content: center; }
  .btn-outline { width: 93px; border: 1.5px solid var(--white); }
  .btn-solid { width: 94px; background: var(--blue-deep); }

  .services { position: absolute; top: 357px; left: 139px; display: flex; gap: 22px; }
  .service-card { width: 170px; height: 151px; background: var(--card-bg); padding: 20px 8px 0 8px; color: var(--white); }
  .service-icon { height: 20px; }
  .service-title { margin-top: 14px; font-size: 9.6px; font-weight: 700; letter-spacing: -0.1px; white-space: nowrap; }
  .service-text { margin-top: 8px; font-size: 7px; line-height: 13.6px; color: var(--muted-white); }

  .feature { position: absolute; left: 0; width: 1025px; }
  .feature-financial { top: 560px; height: 330px; background: var(--white); }
  .feature-relationship { top: 890px; height: 310px; background: var(--blue-band); }
  .feature-copy { position: absolute; width: 275px; }
  .feature-heading { font-size: 18.5px; line-height: 24px; font-weight: 700; }
  .feature-body { margin-top: 8px; font-size: 8.4px; line-height: 17.4px; }
  .feature-financial .feature-copy { left: 224px; top: 90px; }
  .feature-financial .feature-heading { color: var(--heading-dark); }
  .feature-financial .feature-body { color: var(--body-grey); }
  .feature-relationship .feature-copy { left: 528px; top: 72px; }
  .feature-relationship .feature-heading { color: var(--white); }
  .feature-relationship .feature-body { color: var(--muted-white); }
  .btn-know { margin-top: 30px; width: 82px; height: 27px; font-size: 6.5px; font-weight: 900; letter-spacing: 0.3px; color: var(--white); display: flex; align-items: center; justify-content: center; }
  .feature-financial .btn-know { background: linear-gradient(90deg, var(--btn-grad-a), var(--btn-grad-b)); }
  .feature-relationship .btn-know { background: var(--btn-light); margin-top: 20px; }
  .feature-photo { position: absolute; width: 272px; height: 181px; }
  .feature-financial .feature-photo { left: 528px; top: 85px; background: linear-gradient(135deg, #2a2c36 0%, #5a4a44 45%, #8a6a4e 75%, #3c3a44 100%); }
  .feature-relationship .feature-photo { left: 224px; top: 65px; background: linear-gradient(135deg, #6e88a8 0%, #c9d3de 45%, #8b97a6 75%, #4e5a6e 100%); }
</style>
</head>
<body>
  <section class="hero">
    <div class="hero-photo" role="img" aria-label="Blue-tinted photo of a desk with a laptop, a small plant and a person using a phone"></div>
    <p class="hero-eyebrow">Lorem ipsum dolor sit amet</p>
    <h1 class="hero-title">Business Planning &amp;<br>Software Consultant</h1>
    <p class="hero-lead">Lorem ipsum dolor sit amet, consectetur adipiscing elit, sed do eiusmod tempor incididunt ut labore et dolore magna aliqua. Ut enim ad minim veniam.</p>
    <div class="hero-actions">
      <span class="btn-outline">Contact Us</span>
      <span class="btn-solid">Our Services</span>
    </div>

    <div class="services">
      <article class="service-card">
        <svg class="service-icon" width="18" height="20" viewBox="0 0 18 20" fill="none" stroke="#fff" stroke-width="1.6"><rect x="2" y="2" width="4" height="11" rx="2"/><path d="M4 13v5"/><rect x="11" y="2" width="4" height="11" rx="2"/><path d="M13 13l-2 5"/></svg>
        <h2 class="service-title">COSTUM SOLUTION DELIVERY</h2>
        <p class="service-text">Vellora offers a range of services focused on helping businesses and organizations deliver software solutions to their customers or users.</p>
      </article>
      <article class="service-card">
        <svg class="service-icon" width="20" height="20" viewBox="0 0 20 20"><rect x="1" y="5" width="18" height="10" rx="1.5" fill="#fff"/><circle cx="6" cy="10" r="2" fill="#1a4a8e"/><circle cx="14" cy="10" r="2" fill="#1a4a8e"/><path d="M8.5 15 10 12.5 11.5 15z" fill="#1a4a8e"/></svg>
        <h2 class="service-title">STAFF AUGMENTATION</h2>
        <p class="service-text">Let Vellora help you supplement your existing software development teams with additional resources and expertise. We provided access to experienced</p>
      </article>
      <article class="service-card">
        <svg class="service-icon" width="22" height="20" viewBox="0 0 22 20" fill="#fff"><circle cx="11" cy="6" r="3"/><path d="M5.5 16c0-3 2.5-5 5.5-5s5.5 2 5.5 5z"/><circle cx="4.5" cy="8" r="2.2"/><path d="M0.5 16c0-2.4 1.8-4 4-4 .8 0 1.4.2 2 .5-1 1-1.5 2.2-1.6 3.5z"/><circle cx="17.5" cy="8" r="2.2"/><path d="M21.5 16c0-2.4-1.8-4-4-4-.8 0-1.4.2-2 .5 1 1 1.5 2.2 1.6 3.5z"/></svg>
        <h2 class="service-title">TEAM STONGER ANALYSE</h2>
        <p class="service-text">Let Vellora help you supplement your existing software development teams with additional resources and expertise. We provided access to experienced</p>
      </article>
      <article class="service-card">
        <svg class="service-icon" width="18" height="20" viewBox="0 0 18 20" fill="#fff"><rect x="5" y="2" width="6" height="16"/><rect x="1" y="8" width="4" height="10"/><rect x="11" y="6" width="5" height="12"/><g fill="#1a4a8e"><rect x="6.5" y="4" width="1.2" height="1.6"/><rect x="8.5" y="4" width="1.2" height="1.6"/><rect x="6.5" y="8" width="1.2" height="1.6"/><rect x="8.5" y="8" width="1.2" height="1.6"/><rect x="6.5" y="12" width="1.2" height="1.6"/><rect x="8.5" y="12" width="1.2" height="1.6"/><rect x="2.4" y="11" width="1.2" height="1.6"/><rect x="12.8" y="9" width="1.2" height="1.6"/><rect x="12.8" y="13" width="1.2" height="1.6"/></g></svg>
        <h2 class="service-title">BEST PATHNER BUSINESS</h2>
        <p class="service-text">Let Vellora help you supplement your existing software development teams with additional resources and expertise. We provided access to experienced</p>
      </article>
    </div>
  </section>

  <section class="feature feature-financial">
    <div class="feature-copy">
      <h2 class="feature-heading">Software for Financial Data</h2>
      <p class="feature-body">Lorem ipsum dolor sit amet, consectetur adipiscing elit, sed do eiusmod tempor incididunt ut labore et dolore magna aliqua. Ut enim ad minim veniam, quis nostrud exercitation ullamco laboris. Duis aute irure dolor in reprehenderit in voluptate velit esse cillum dolore eu fugiat nulla pariatur.</p>
      <span class="btn-know">KNOW MORE</span>
    </div>
    <div class="feature-photo" role="img" aria-label="Photo of colleagues talking at a wooden table with an open laptop"></div>
  </section>

  <section class="feature feature-relationship">
    <div class="feature-photo" role="img" aria-label="Photo of two people reviewing printed charts beside laptops"></div>
    <div class="feature-copy">
      <h2 class="feature-heading">Build a Stronger Relationship<br>with Your Customers</h2>
      <p class="feature-body">Lorem ipsum dolor sit amet, consectetur adipiscing elit, sed do eiusmod tempor incididunt ut labore et dolore magna aliqua. Duis aute irure dolor in reprehenderit in voluptate velit esse cillum dolore eu fugiat nulla pariatur. Excepteur sint occaecat cupidatat non proident.</p>
      <span class="btn-know">KNOW MORE</span>
    </div>
  </section>
</body>
</html>
```